Assisted living facility needs a business card design

We need a business card design for an assisted living facility in Los Angeles. We have a logo selected but we would like a business card design that will leave a lasting impression on families looking to place their elderly loved ones in our care as well as on other facility providers who may refer their elderly residents to our facility.

```html
<!DOCTYPE html>
<html lang="en">
<head>
<meta charset="utf-8">
<title>Harborview Crest Senior Living – Business Card</title>
<link rel="stylesheet" href="https://fonts.googleapis.com/css2?family=Cinzel:wght@400;700&family=Open+Sans:wght@400;600&display=swap">
<style>
  :root {
    --stage: #e9eaec;
    --brand-blue: #0d78c4;
    --deep-blue: #0a58b0;
    --card-black: #1b1b1c;
    --wave-grey: #7a7b7e;
    --ink-light: #ffffff;
    --ink-soft: #e6e6e6;
  }
  * { box-sizing: border-box; margin: 0; padding: 0; }
  html, body {
    width: 1200px; height: 801px; overflow: hidden;
    background: var(--stage);
  }
  .stage {
    position: relative; width: 1200px; height: 801px;
    display: flex; align-items: center; justify-content: center; gap: 40px;
  }
  .card {
    position: relative; width: 540px; height: 309px;
    border-radius: 16px; overflow: hidden;
    box-shadow: 0 8px 24px rgba(0,0,0,.18);
  }
  .card-front {
    background: var(--brand-blue);
    display: flex; align-items: center; justify-content: center;
  }
  .brand-name {
    font-family: "Cinzel", serif; font-weight: 400;
    letter-spacing: 2px; text-transform: uppercase; text-align: center;
    line-height: 1.25;
  }
  .card-front .brand-name { color: var(--ink-light); font-size: 34px; }
  .card-back { background: var(--card-black); }
  .back-wave { position: absolute; inset: 0; width: 100%; height: 100%; }
  .card-back .brand-name {
    position: absolute; left: 30px; top: 140px; width: 290px;
    color: var(--brand-blue); font-size: 21px;
  }
  .divider {
    position: absolute; left: 340px; top: 36px; width: 1.5px; height: 150px;
    background: var(--deep-blue);
  }
  .contact {
    position: absolute; left: 356px; top: 32px;
    font-family: "Open Sans", sans-serif; color: var(--ink-soft);
    font-size: 11.5px; line-height: 1.5;
  }
  .person-name {
    font-family: "Cinzel", serif; font-weight: 700;
    color: var(--brand-blue); font-size: 17px; letter-spacing: .5px; line-height: 1.1;
  }
  .person-role { font-size: 12px; margin-bottom: 14px; }
  .contact-list { list-style: none; margin-bottom: 12px; }
  .contact-list li { display: flex; align-items: center; gap: 7px; }
  .contact-list svg { width: 10px; height: 10px; flex: none; }
  .address { font-size: 11.5px; }
</style>
</head>
<body>
<main class="stage">
  <section class="card card-front" aria-label="Card front">
    <p class="brand-name">Harborview Crest<br>Senior Living</p>
  </section>

  <section class="card card-back" aria-label="Card back">
    <svg class="back-wave" viewBox="0 0 540 309" preserveAspectRatio="none" aria-hidden="true">
      <path d="M150 309 C290 300 370 285 425 250 C470 222 500 206 540 202 L540 309 Z" fill="var(--wave-grey)"/>
      <path d="M165 309 C300 304 382 290 435 258 C478 232 506 218 540 214 L540 309 Z" fill="var(--deep-blue)"/>
    </svg>
    <p class="brand-name">Harborview Crest<br>Senior Living</p>
    <div class="divider"></div>
    <div class="contact">
      <p class="person-name">DANIEL REYES</p>
      <p class="person-role">Managing Director</p>
      <ul class="contact-list">
        <li><svg viewBox="0 0 10 10"><path d="M2 0.5 L3.6 2.6 L2.8 3.6 C3.4 5 4.8 6.5 6.3 7.2 L7.3 6.3 L9.5 7.9 L8.4 9.5 C4.5 9.3 0.7 5.5 0.5 1.6 Z" fill="var(--brand-blue)"/></svg>123 456 789</li>
        <li><svg viewBox="0 0 10 10"><rect x="0.5" y="2" width="9" height="6.5" fill="var(--brand-blue)"/><path d="M0.5 2 L5 5.6 L9.5 2" stroke="var(--card-black)" stroke-width=".8" fill="none"/></svg>info@yourmail.com</li>
        <li><svg viewBox="0 0 10 10"><circle cx="5" cy="5" r="4.5" fill="var(--brand-blue)"/><path d="M0.5 5 H9.5 M5 0.5 C2.5 3 2.5 7 5 9.5 M5 0.5 C7.5 3 7.5 7 5 9.5" stroke="var(--card-black)" stroke-width=".7" fill="none"/></svg>www.yourwebsite.com</li>
      </ul>
      <p class="address">Your address, City<br>State, Zip 1234</p>
    </div>
  </section>
</main>
</body>
</html>
```